Young Accounting firm needing a captivating business card

We need a business card design that forces the person to look at the card because its either gold foil, plastic, or lettering pop up etc. We already have a logo with a specific gold color and we need to make it pop. We are an accounting firm. I need the words" accounting, payroll, licenses, audits, taxes" somewhere on the business card so as to describe what we do- preferably on the side where the logo is at.

Industry/Entity Type

Accounting

Contact Information for Business Card

Address 48276 9th Ave S Ste 305, Federal Way, WA 98117
Business Phone (360)418-2096
Fax (360)418-2157
Office Cell Phone (360)586-7319

Font styles to use
Serif

Colors
85abd2

Requirements
Must have
• It should state
• "Accounting" "Taxes" "Audits" "Licenses" "Payroll"
Nice to have
• Matte with gold foil, different textures, With Either a textured ivory background or gray blue slate background
Should not have
• colorful colors

```html
<!DOCTYPE html>
<html lang="en">
<head>
<meta charset="utf-8">
<title>Ledgerwise – Business Card</title>
<link rel="stylesheet" href="https://fonts.googleapis.com/css2?family=Lato:wght@400;700&display=swap">
<style>
  :root {
    --backdrop: #3a3b37;
    --card: #121212;
    --card-edge: #1c1c1c;
    --gold: #c9a43a;
    --white: #f2f2f2;
    --muted: #b9b9b9;
  }
  * { margin: 0; padding: 0; box-sizing: border-box; }
  html, body {
    width: 1200px; height: 825px; overflow: hidden;
    background: var(--backdrop);
    font-family: "Lato", sans-serif;
  }
  .canvas { position: relative; width: 1200px; height: 825px; }

  .card {
    position: absolute;
    width: 540px; height: 309px;
    background: var(--card);
    border: 1px solid var(--card-edge);
    border-radius: 6px;
    box-shadow: 0 18px 40px rgba(0,0,0,.45);
  }
  .card--front { left: 40px; top: 130px; }
  .card--back  { left: 620px; top: 386px; }

  .brand {
    display: flex; align-items: center; gap: 12px;
    color: var(--gold); font-weight: 700;
  }
  .brand__mark { background: var(--gold); }

  /* Front */
  .card--front .brand {
    position: absolute; left: 0; right: 0; top: 100px;
    justify-content: center; font-size: 46px; letter-spacing: .5px;
  }
  .card--front .brand__mark { width: 38px; height: 38px; }
  .services {
    position: absolute; left: 0; right: 0; top: 180px;
    text-align: center; color: var(--white);
    font-size: 13px; letter-spacing: .6px;
  }
  .services span { margin: 0 6px; color: var(--muted); }

  /* Back */
  .person { position: absolute; left: 36px; top: 34px; }
  .person__name { color: var(--white); font-weight: 700; font-size: 17px; }
  .person__title { color: var(--gold); font-size: 11px; letter-spacing: .8px; margin-top: 2px; }
  .person__rule { width: 34px; height: 2px; background: var(--gold); margin-top: 12px; }

  .contacts { position: absolute; left: 36px; top: 176px; list-style: none; }
  .contacts li {
    display: flex; align-items: center; gap: 10px;
    color: var(--white); font-size: 14px; line-height: 24px;
  }
  .contacts svg { width: 12px; height: 12px; fill: var(--gold); flex: none; }

  .card--back .brand {
    position: absolute; right: 40px; top: 118px;
    font-size: 30px;
  }
  .card--back .brand__mark { width: 24px; height: 24px; }

  .address {
    position: absolute; right: 40px; bottom: 30px;
    color: var(--white); font-size: 14px; line-height: 22px; text-align: right;
  }
</style>
</head>
<body>
<main class="canvas">

  <section class="card card--front" aria-label="Card front">
    <div class="brand"><span class="brand__mark"></span><span class="brand__name">Ledgerwise</span></div>
    <p class="services">Accounting<span>|</span>Taxes<span>|</span>Audits<span>|</span>Licenses<span>|</span>Payroll</p>
  </section>

  <section class="card card--back" aria-label="Card back">
    <div class="person">
      <p class="person__name">Your Name</p>
      <p class="person__title">JOB TITLE</p>
      <div class="person__rule"></div>
    </div>

    <ul class="contacts">
      <li><svg viewBox="0 0 12 12" aria-hidden="true"><path d="M2.5 0.5l2 2.2-1 1.3c.7 1.6 2 2.9 3.5 3.6l1.3-1 2.2 2-1.2 2.4C4.5 10.6 1.4 7.5.2 2.2z"/></svg>(360)418-2096</li>
      <li><svg viewBox="0 0 12 12" aria-hidden="true"><path d="M2.5 0.5l2 2.2-1 1.3c.7 1.6 2 2.9 3.5 3.6l1.3-1 2.2 2-1.2 2.4C4.5 10.6 1.4 7.5.2 2.2z"/></svg>(360)418-2157</li>
      <li><svg viewBox="0 0 12 12" aria-hidden="true"><path d="M3 0h6v12H3zM4.2 1.2v8h3.6v-8z"/></svg>(360)586-7319</li>
      <li><svg viewBox="0 0 12 12" aria-hidden="true"><path d="M0 2h12v8H0zM1 3v.4l5 3.4 5-3.4V3z"/></svg>youremail@ledgerwise.com</li>
    </ul>

    <div class="brand"><span class="brand__mark"></span><span class="brand__name">Ledgerwise</span></div>

    <p class="address">48276 9th Ave S Ste 305<br>Federal Way, WA 98117</p>
  </section>

</main>
</body>
</html>
```